WANTED: The Best Mobile App Designers

We are looking for the best mobile app designers.

This is a small test job to test your skills and the winner will be given ongoing work which means ongoing work and revenue for you!

If you do not feel you are the BEST please DO NOT APPLY as we are only looking for "the" best mobile app designers with experience.

Attached is a test spec for a design we need.

Look forward to seeing your skills and creating a long term relationship.

Target Market(s)

General consumers who are looking to sell their unwanted items to make extra cash

Industry/Entity Type

Work

Requirements
Must have
• The designs must match and look great with the attached logo.

Design must be top quality and give the impression of a billion dollar company.

```html
<!DOCTYPE html>
<html lang="en">
<head>
<meta charset="utf-8">
<title>Swapnest – App Screens</title>
<link href="https://fonts.googleapis.com/css2?family=Open+Sans:wght@400;600;700&display=swap" rel="stylesheet">
<style>
  :root {
    --canvas-bg: #ede7e4;
    --screen-grey-top: #d9dcdf;
    --screen-grey-bottom: #a9aeb3;
    --ink: #2a2a2a;
    --ink-soft: #555;
    --red: #c8232c;
    --red-dark: #a51d24;
    --red-header-top: #d25a5c;
    --red-header-bottom: #b3262c;
    --blue-bar: #1a8fc9;
    --blue-bar-dark: #0f76ab;
    --kinnect-blue: #4a6fb5;
    --buzzline-blue: #1ba5e0;
    --email-red: #d24b2e;
    --green: #2e8a1c;
    --green-light: #4cae2c;
    --tile-frame: #d8c8b8;
    --panel: #f3f0ec;
    --row: #f7f6f4;
    --line: #d6d3cf;
    --status: #111;
  }
  * { box-sizing: border-box; margin: 0; padding: 0; }
  html, body { width: 1200px; height: 881px; overflow: hidden; }
  body {
    background: var(--canvas-bg);
    font-family: "Open Sans", Arial, sans-serif;
    color: var(--ink);
    position: relative;
  }
  .screen {
    position: absolute;
    top: 200px;
    width: 320px;
    height: 480px;
    overflow: hidden;
    background: linear-gradient(var(--screen-grey-top), var(--screen-grey-bottom));
    box-shadow: 0 10px 30px rgba(0,0,0,.18);
  }
  .screen--welcome { left: 60px; }
  .screen--offer { left: 440px; }
  .screen--checkout { left: 820px; }

  .status-bar {
    height: 20px;
    background: linear-gradient(#3a3a3a, var(--status));
    color: #fff;
    font-size: 12px;
    font-weight: 700;
    display: flex;
    align-items: center;
    justify-content: center;
    position: relative;
  }
  .status-bar .signal { position: absolute; left: 6px; top: 6px; display: flex; gap: 1px; align-items: flex-end; }
  .status-bar .signal i { display: block; width: 3px; background: #fff; }
  .status-bar .battery { position: absolute; right: 6px; top: 6px; width: 18px; height: 8px; border: 1px solid #fff; padding: 1px; }
  .status-bar .battery::after { content: ""; display: block; height: 100%; background: #fff; }

  /* Welcome screen */
  .brand { display: flex; align-items: center; justify-content: center; gap: 8px; margin-top: 28px; }
  .brand__dot { width: 30px; height: 30px; border-radius: 50%; background: var(--blue-bar); }
  .brand__name { font-size: 28px; font-weight: 700; color: var(--red); }
  .tagline { text-align: center; font-size: 14px; color: var(--ink); margin-top: 10px; }
  .tiles { position: absolute; top: 132px; left: -14px; width: 348px; display: grid; grid-template-columns: repeat(4, 81px); gap: 8px; }
  .tile { height: 68px; border: 4px solid var(--tile-frame); position: relative; }
  .tile__photo { position: absolute; inset: 0; background: linear-gradient(135deg, #4a4a4a, #151515); }
  .tile__label {
    position: absolute; left: 0; bottom: 4px;
    background: var(--tile-frame); color: #3a3028;
    font-size: 6.5px; line-height: 1.1; padding: 2px 3px; text-transform: uppercase;
  }
  .social { position: absolute; top: 300px; left: 35px; width: 250px; display: flex; flex-direction: column; gap: 12px; }
  .social__btn {
    height: 32px; border-radius: 2px; color: #fff; font-size: 11px; font-weight: 600;
    display: flex; align-items: center; justify-content: center; gap: 8px;
    box-shadow: 0 1px 2px rgba(0,0,0,.25);
  }
  .social__btn--kinnect { background: var(--kinnect-blue); }
  .social__btn--buzzline { background: var(--buzzline-blue); }
  .social__btn--email { background: var(--email-red); }

  /* Offer screen */
  .app-header {
    height: 40px;
    background: linear-gradient(var(--red-header-top), var(--red-header-bottom));
    display: flex; align-items: center; gap: 8px; padding: 0 10px;
  }
  .search { flex: 1; height: 22px; border-radius: 11px; background: #fff; position: relative; }
  .search svg { position: absolute; right: 8px; top: 5px; }
  .category {
    width: 88px; height: 22px; border-radius: 4px; background: #ddd;
    font-size: 8px; color: #777; display: flex; align-items: center; padding-left: 8px; position: relative;
  }
  .category::after { content: "⇕"; position: absolute; right: 6px; font-size: 9px; color: #555; }
  .banner {
    position: absolute; top: 68px; left: 25px; width: 270px; height: 225px;
    background: #fff; border: 1px solid #bbb; overflow: hidden;
  }
  .banner__visual { position: absolute; inset: 0; background: linear-gradient(90deg, #e4e4e4, #b7b7b7 45%, #6f8f4a 70%, #2e3a20); }
  .banner__tag {
    position: absolute; top: 18px; left: 0; background: var(--red); color: #fff;
    padding: 3px 10px 3px 10px; line-height: 1;
  }
  .banner__tag strong { display: block; font-size: 12px; font-weight: 700; }
  .banner__tag span { display: block; font-size: 7px; margin-top: 1px; }
  .banner__category {
    position: absolute; top: 150px; left: 0; background: #4a3a36; color: #fff;
    font-size: 8px; padding: 3px 18px 3px 18px;
  }
  .banner__deal {
    position: absolute; top: 164px; left: 0; background: #fff; padding: 2px 8px;
    display: flex; align-items: center; gap: 4px;
  }
  .banner__deal b { font-size: 31px; color: var(--red); font-weight: 700; line-height: 1; }
  .banner__deal span { font-size: 13px; line-height: 1; color: #555; }
  .banner__deal span em { font-style: normal; color: var(--red); font-weight: 700; }
  .pager {
    position: absolute; top: 305px; left: 90px; width: 135px; height: 18px;
    background: linear-gradient(#aaa, #6c6c6c); border-radius: 3px;
    display: flex; justify-content: center; align-items: center; gap: 14px;
    font-size: 9px; font-weight: 700; color: #222;
  }
  .pager .is-active { background: #fff; border: 2px solid var(--red); padding: 0 4px; }
  .countdown {
    position: absolute; top: 345px; left: 0; width: 320px; height: 58px; background: #f6f5f3;
    display: flex; align-items: center; justify-content: space-between; padding: 0 20px 0 22px;
  }
  .countdown p { font-size: 11px; font-weight: 700; line-height: 1.35; color: #333; }
  .bid-btn {
    width: 100px; height: 24px; border-radius: 12px;
    background: linear-gradient(var(--green-light), var(--green)); color: #fff;
    font-size: 11px; font-weight: 700; display: flex; align-items: center; justify-content: center;
  }
  .nav-bar {
    position: absolute; bottom: 0; left: 0; width: 320px; height: 42px;
    background: linear-gradient(var(--blue-bar), var(--blue-bar-dark));
    display: flex;
  }
  .nav-bar span {
    flex: 1; color: #fff; font-size: 16px; display: flex; align-items: center; justify-content: center;
  }
  .nav-bar span + span { border-left: 1px solid rgba(0,0,0,.2); }

  /* Checkout screen */
  .checkout-title {
    height: 40px; background: linear-gradient(var(--red-header-top), var(--red-header-bottom));
    color: #fff; font-size: 17px; text-align: center; line-height: 40px; letter-spacing: .5px;
  }
  .order { margin: 8px 14px 0; background: var(--panel); border-radius: 3px; box-shadow: 0 1px 2px rgba(0,0,0,.2); }
  .order + .order { margin-top: 8px; }
  .order__head, .order__row {
    height: 24px; display: flex; align-items: center; justify-content: space-between;
    padding: 0 8px; font-size: 7.5px; text-transform: uppercase; color: #333;
    border-bottom: 1px solid var(--line); background: var(--row);
  }
  .order__row .label { display: flex; align-items: center; gap: 6px; }
  .toggle {
    width: 12px; height: 12px; border-radius: 50%; background: #e2e2e2; color: #666;
    font-size: 9px; line-height: 12px; text-align: center;
  }
  .order__item { display: flex; gap: 10px; padding: 8px; height: 88px; border-bottom: 1px solid var(--line); }
  .order__photo { width: 50px; height: 70px; background: linear-gradient(135deg, #555, #1a1a1a 60%, #c9a23a); border-radius: 3px; }
  .price { flex: 1; display: grid; grid-template-columns: 1fr auto; font-size: 6.5px; color: #444; row-gap: 1px; align-content: start; padding-top: 6px; }
  .price .total { font-weight: 700; margin-top: 6px; }
</style>
</head>
<body>

<section class="screen screen--welcome" aria-label="Welcome screen">
  <div class="status-bar">
    <span class="signal"><i style="height:3px"></i><i style="height:4px"></i><i style="height:6px"></i><i style="height:7px"></i></span>
    9:00 AM
    <span class="battery"></span>
  </div>
  <div class="brand">
    <span class="brand__dot"></span>
    <span class="brand__name">Swapnest</span>
  </div>
  <p class="tagline">Sell, buy, rent anything!</p>
  <div class="tiles">
    <div class="tile"><div class="tile__photo" role="img" aria-label="Smartphone product photo"></div></div>
    <div class="tile"><div class="tile__photo" role="img" aria-label="Leather shoes product photo"></div><span class="tile__label">Exclusive<br>offers</span></div>
    <div class="tile"><div class="tile__photo" role="img" aria-label="Smartphones product photo"></div><span class="tile__label">Deals of<br>the month</span></div>
    <div class="tile"><div class="tile__photo" role="img" aria-label="Product photo"></div><span class="tile__label">Exclusive<br>offers</span></div>
    <div class="tile"><div class="tile__photo" role="img" aria-label="Product photo"></div></div>
    <div class="tile"><div class="tile__photo" role="img" aria-label="Wristwatch product photo"></div><span class="tile__label">Limited<br>collection</span></div>
    <div class="tile"><div class="tile__photo" role="img" aria-label="Leather goods product photo" style="background:linear-gradient(135deg,#c9a27a,#5c4636)"></div><span class="tile__label">New<br>arrivals</span></div>
    <div class="tile"><div class="tile__photo" role="img" aria-label="Product photo"></div><span class="tile__label">Limited<br>collection</span></div>
  </div>
  <div class="social">
    <a class="social__btn social__btn--kinnect">Login with Kinnect</a>
    <a class="social__btn social__btn--buzzline">Login with Buzzline</a>
    <a class="social__btn social__btn--email">
      <svg width="14" height="10" viewBox="0 0 14 10"><rect x=".5" y=".5" width="13" height="9" fill="#fff"/><path d="M.5.5 7 6 13.5.5" fill="none" stroke="#d24b2e"/></svg>
      Sign in with email
    </a>
  </div>
</section>

<section class="screen screen--offer" aria-label="Offer screen">
  <div class="status-bar">
    <span class="signal"><i style="height:3px"></i><i style="height:4px"></i><i style="height:6px"></i><i style="height:7px"></i></span>
    9:00 AM
    <span class="battery"></span>
  </div>
  <header class="app-header">
    <div class="search">
      <svg width="11" height="11" viewBox="0 0 11 11"><circle cx="4.5" cy="4.5" r="3.5" fill="none" stroke="#999" stroke-width="1.5"/><path d="M7 7l3 3" stroke="#999" stroke-width="1.5"/></svg>
    </div>
    <div class="category">All Categories</div>
  </header>
  <div class="banner">
    <div class="banner__visual" role="img" aria-label="Norvo smartphone shown front and back"></div>
    <div class="banner__tag"><strong>EXCLUSIVE OFFERS</strong><span>OF THE MONTH</span></div>
    <div class="banner__category">MOBILE DEVICES</div>
    <div class="banner__deal"><b>30%</b><span><em>OFF</em> ON<br>SELECTEDRANGE</span></div>
  </div>
  <div class="pager"><span class="is-active">1</span><span>2</span><span>3</span></div>
  <div class="countdown">
    <p>5 days, 15:44:22<br>Time left (Date)</p>
    <span class="bid-btn">Bid Now</span>
  </div>
  <nav class="nav-bar"><span>BACK</span><span>NEXT</span></nav>
</section>

<section class="screen screen--checkout" aria-label="Checkout screen">
  <div class="status-bar">
    <span class="signal"><i style="height:3px"></i><i style="height:4px"></i><i style="height:6px"></i><i style="height:7px"></i></span>
    9:00 AM
    <span class="battery"></span>
  </div>
  <h1 class="checkout-title">CHECKOUT</h1>
  <div class="order">
    <div class="order__head">Norvo mobile phone <span class="toggle">−</span></div>
    <div class="order__item">
      <div class="order__photo" role="img" aria-label="Norvo smartphone photo"></div>
      <div class="price">
        <span>Purchase price:</span><span>300.00 US</span>
        <span>Transaction fees:</span><span>7.00 US</span>
        <span>Shipping and Handling:</span><span>9.00 US</span>
        <span class="total">TOTAL:</span><span class="total">316.00 US</span>
      </div>
    </div>
    <div class="order__row"><span class="label"><svg width="12" height="9" viewBox="0 0 12 9"><rect x=".5" y=".5" width="11" height="8" rx="1" fill="none" stroke="#555"/><rect x=".5" y="2.5" width="11" height="1.5" fill="#555"/></svg>Add a credit card</span><span class="toggle">+</span></div>
    <div class="order__row"><span>Bill</span><span class="toggle">+</span></div>
    <div class="order__row"><span>Ship</span><span class="toggle">+</span></div>
  </div>
  <div class="order">
    <div class="order__head">Other product <span class="toggle">+</span></div>
    <div class="order__row"><span class="label"><svg width="12" height="9" viewBox="0 0 12 9"><rect x=".5" y=".5" width="11" height="8" rx="1" fill="none" stroke="#555"/><rect x=".5" y="2.5" width="11" height="1.5" fill="#555"/></svg>Add a credit card</span><span class="toggle">+</span></div>
    <div class="order__row"><span>Bill</span><span class="toggle">+</span></div>
    <div class="order__row"><span>Ship</span><span class="toggle">+</span></div>
  </div>
  <nav class="nav-bar"><span>BACK</span><span>NEXT</span></nav>
</section>

</body>
</html>
```